Flyer Design

STERLING SHADES
ph:9361 4085
7/41 Pellow Street
Malaga, WA 6069
we need a flyer design for a part broshure part flyer asking for business. well astablished small business for 15years. we manufacture blinds to domestic and commercial. custom made and premium quality. very competitive, free measure and quote even on weekend, plus we offer free fitting to all area. can supply all type of blinds as in big companies. such as roller blinds, roman blinds, timber venetians, slimline venetians, panel glide, vertical blinds, timber shutters etc.

Target Market(s)

new home

Industry/Entity Type

Small Business

Requirements
Nice to have
• a few different type of blinds in partially or part of it may be...

```html
<!DOCTYPE html>
<html lang="en">
<head>
<meta charset="utf-8">
<title>Sterling Shades Flyer</title>
<link rel="stylesheet" href="https://fonts.googleapis.com/css2?family=Lato:wght@400;700;900&family=Noto+Serif:wght@700&family=Tinos:wght@400&display=swap">
<style>
  :root {
    --page-bg: #e6e6e6;
    --blue-deep: #17589e;
    --blue-mid: #2c7cc7;
    --blue-light: #5aa9e6;
    --slate: #3f4850;
    --white: #ffffff;
  }
  * { margin: 0; padding: 0; box-sizing: border-box; }
  html, body { width: 955px; height: 1200px; overflow: hidden; }
  body { background: var(--page-bg); position: relative; }

  .flyer {
    position: absolute; left: 67px; top: 26px;
    width: 705px; height: 987px;
    transform: scale(1.163); transform-origin: 0 0;
    overflow: hidden;
    font-family: "Lato", sans-serif; color: var(--white);
  }
  .flyer-shapes { position: absolute; inset: 0; }
  .line { display: block; white-space: nowrap; }

  .title-banner {
    position: absolute; left: 35px; top: 20px; width: 420px; height: 75px;
    background: var(--blue-mid);
    display: flex; align-items: center; justify-content: center;
  }
  .title-banner h1 {
    font-family: "Noto Serif", serif; font-weight: 700; font-size: 38px;
    letter-spacing: 0.3px; color: var(--white); white-space: nowrap;
  }

  .intro {
    position: absolute; left: 21px; top: 130px;
    font-size: 16px; line-height: 19.8px;
  }
  .range-band {
    position: absolute; left: 0; top: 329px; width: 322px; height: 120px;
    background: var(--blue-light);
    clip-path: polygon(0 0, 290px 0, 322px 100%, 0 100%);
    padding: 10px 0 0 21px;
    font-family: "Tinos", serif; font-size: 16px; line-height: 20px;
  }
  .detail {
    position: absolute; left: 21px; top: 474px;
    font-size: 16px; line-height: 19.7px;
  }
  .note-band {
    position: absolute; left: 0; top: 695px; width: 324px; height: 122px;
    background: var(--blue-light);
    clip-path: polygon(0 0, 288px 0, 324px 100%, 0 100%);
    padding: 9px 0 0 21px;
    font-size: 15.5px; line-height: 20.7px;
  }
  .fine-print {
    position: absolute; left: 23px; top: 830px;
    font-size: 10.5px; line-height: 13px;
  }
  .phone-line {
    position: absolute; left: 21px; top: 858px;
    display: flex; align-items: center; gap: 10px;
    font-weight: 900; font-size: 34px; line-height: 40px;
  }
  .web-line {
    position: absolute; left: 23px; top: 925px;
    display: flex; align-items: center; gap: 14px;
    font-weight: 900; font-size: 32px; line-height: 44px;
    white-space: nowrap;
  }
</style>
</head>
<body>
<div class="flyer">
  <svg class="flyer-shapes" viewBox="0 0 705 987" width="705" height="987">
    <defs>
      <linearGradient id="panel-blue" x1="0" y1="0" x2="1" y2="0">
        <stop offset="0" stop-color="#1d63ad"/>
        <stop offset="1" stop-color="#2a78c4"/>
      </linearGradient>
      <linearGradient id="room-tone" x1="0" y1="0" x2="0.6" y2="1">
        <stop offset="0" stop-color="#eeeae2"/>
        <stop offset="0.55" stop-color="#cfc9bd"/>
        <stop offset="1" stop-color="#7c6f5f"/>
      </linearGradient>
      <linearGradient id="timber-tone" x1="0" y1="0" x2="1" y2="1">
        <stop offset="0" stop-color="#c9894a"/>
        <stop offset="1" stop-color="#7a4a22"/>
      </linearGradient>
      <linearGradient id="slat-tone" x1="0" y1="0" x2="1" y2="1">
        <stop offset="0" stop-color="#f4f7fa"/>
        <stop offset="1" stop-color="#a9b6c2"/>
      </linearGradient>
      <linearGradient id="window-tone" x1="0" y1="0" x2="0" y2="1">
        <stop offset="0" stop-color="#e8ecef"/>
        <stop offset="1" stop-color="#9aa3a8"/>
      </linearGradient>
    </defs>

    <rect class="panel" width="705" height="987" fill="url(#panel-blue)"/>

    <polygon class="room-photo" role="img" aria-label="Photo of a bright dining room with vertical blinds"
      points="345,0 705,0 705,922 496,922" fill="url(#room-tone)"/>

    <polygon class="stripe-white" points="300,0 312,0 474,987 462,987" fill="var(--white)"/>
    <polygon class="stripe-slate" points="312,0 333,0 495,987 474,987" fill="var(--slate)"/>
    <polygon class="stripe-white" points="333,0 345,0 507,987 495,987" fill="var(--white)"/>

    <rect class="corner-band" x="480" y="922" width="225" height="65" fill="#1f6fb8"/>

    <rect class="footer-rule" x="0" y="906" width="452" height="6" fill="var(--white)"/>
    <polygon class="footer-bar" points="0,912 451,912 462,987 0,987" fill="var(--slate)"/>

    <g class="badge">
      <circle cx="370" cy="252" r="95" fill="var(--white)"/>
      <circle cx="370" cy="252" r="86" fill="var(--slate)"/>
      <circle cx="370" cy="252" r="74" fill="url(#timber-tone)" role="img" aria-label="Photo of timber venetian blind slats"/>
    </g>
    <g class="badge">
      <circle cx="412" cy="522" r="95" fill="var(--white)"/>
      <circle cx="412" cy="522" r="86" fill="var(--blue-deep)"/>
      <circle cx="412" cy="522" r="74" fill="url(#slat-tone)" role="img" aria-label="Photo of white slimline venetian blinds"/>
    </g>
    <g class="badge">
      <circle cx="452" cy="757" r="92" fill="var(--white)"/>
      <circle cx="452" cy="757" r="83" fill="var(--slate)"/>
      <circle cx="452" cy="757" r="71" fill="url(#window-tone)" role="img" aria-label="Photo of vertical blinds over glass doors"/>
    </g>
  </svg>

  <div class="title-banner"><h1>STERLING SHADES</h1></div>

  <p class="intro">
    <span class="line">STERLING SHADES is well astablished</span>
    <span class="line">small business for 15years.we</span>
    <span class="line">manufacture blinds to domestic and</span>
    <span class="line">commercial. custom made and</span>
    <span class="line">premium quality. very</span>
    <span class="line">competitive, free measure</span>
    <span class="line">and quote even on weekend,</span>
    <span class="line">plus we offer free fitting to all</span>
    <span class="line">area.</span>
  </p>

  <div class="range-band">
    <p>
      <span class="line">can supply all type of blinds as in</span>
      <span class="line">big companies. such as roller blinds,</span>
      <span class="line">roman blinds, timber venetians,</span>
      <span class="line">slimline venetians, panel glide,</span>
      <span class="line">vertical blinds, timber shutters etc.</span>
    </p>
  </div>

  <p class="detail">
    <span class="line">Lorem Ipsum is simply dummy text of</span>
    <span class="line">the printing and typesetting industry.</span>
    <span class="line">Lorem Ipsum has been the industry's</span>
    <span class="line">standard dummy text ever since the</span>
    <span class="line">1500s, when an unknown printer took a</span>
    <span class="line">galley of type and scrambled it to make a</span>
    <span class="line">type specimen book. It has survived not</span>
    <span class="line">only five centuries, but also the leap into</span>
    <span class="line">electronic typesetting, remaining</span>
    <span class="line">essentially unchanged.</span>
  </p>

  <div class="note-band">
    <p>
      <span class="line">Lorem Ipsum is simply dummy</span>
      <span class="line">text of the printing and typesetting</span>
      <span class="line">industry. Lorem Ipsum is simply</span>
      <span class="line">dummy text of the printing and</span>
      <span class="line">typesetting industry.</span>
    </p>
  </div>

  <p class="fine-print">
    <span class="line">Lorem Ipsum is simply dummy text of the printing</span>
    <span class="line">and typesetting text of the printing and typesetting</span>
  </p>

  <div class="phone-line">
    <svg class="icon-phone" width="30" height="30" viewBox="0 0 30 30" aria-hidden="true">
      <rect width="30" height="30" rx="6" fill="var(--white)"/>
      <path d="M10 6c1.5 0 3.5 4 3.5 5s-2 1.5-2 2.5 3 5.5 4.5 5.5 1.5-2 2.5-2 4.5 2 4.5 3.5-2 3.5-4 3.5C13 24 6 16 6 10c0-2 2.5-4 4-4z" fill="var(--blue-deep)"/>
    </svg>
    <span>000-000-000</span>
  </div>

  <div class="web-line">
    <svg class="icon-mail" width="34" height="22" viewBox="0 0 34 22" aria-hidden="true">
      <rect x="1" y="1" width="32" height="20" fill="none" stroke="var(--white)" stroke-width="2"/>
      <path d="M1 1l16 12L33 1M1 21l12-10M33 21L21 11" fill="none" stroke="var(--white)" stroke-width="2"/>
    </svg>
    <span>www.sterlingshades.net</span>
  </div>
</div>
</body>
</html>
```